Brochure Design Project

We are a consulting engineering company and need to have our current company brochure updated and made to look a lot more professional.

We provide design and documentation of electrical, lighting, mechanical, hydraulic, fire, services to architects, interior designers, building owners and managers.

We are launching an updated website shortly and want a print brochure to send to clients.

Attached is our current brochure for reference.
Updates

The recent projects section should be renamed to "Completed Projects". Space should be allowed for 8 projects. I have uploaded 7 of these images and a new image will follow shortly.

We would like to include an image for each of our company services. I have uploaded 9 new images:

1. Electrical
2. Mechanical
3. Communications
4. Fire
5. Security
6. Lighting
7. Hydraulics
8. Computer Suite
9. Building Assessments

Target Market(s)

Architects, Interior Designers, Consultants, Professionals

Industry/Entity Type

Building

Requirements
Must have
• Very professional look
Simple and easy to read layout
Similar look and feel to our new website which is soon to be launched : http://www.sitehaven.co.uk/rkm/
Examples of our recent projects - around 6 projects with 1 or 2 photos per project. Will upload these soon.
A3 size, double sided with centre fold
Should not have
• Bright colours
Any comics or similar

```html
<!DOCTYPE html>
<html lang="en">
<head>
<meta charset="utf-8">
<title>rkm Consulting Services – Brochure</title>
<link rel="stylesheet" href="https://fonts.googleapis.com/css2?family=Exo+2:ital,wght@0,300;0,400;0,600;1,300;1,400;1,600&display=swap">
<style>
  :root{
    --ink-dark:#2b2a28;
    --band-grey:#dcdcdc;
    --paper:#f4f4f4;
    --paper-white:#fbfbfb;
    --text-grey:#8d8d8d;
    --text-mid:#6d6d6d;
    --text-soft:#a9a9a9;
    --logo-grey:#c9c9c9;
    --lime:#a8c62a;
    --lime-deep:#7f9a1c;
    --stage:#e9e9e9;
  }
  *{box-sizing:border-box;margin:0;padding:0}
  html,body{width:984px;height:1200px;overflow:hidden}
  body{background:var(--stage);font-family:"Exo 2",sans-serif;color:var(--text-grey);position:relative}

  /* ---------- Cover ---------- */
  .cover{position:absolute;left:297px;top:16px;width:390px;height:552px;background:linear-gradient(#f7f7f7,#e7e7e7);box-shadow:0 2px 8px rgba(0,0,0,.18);overflow:hidden}
  .cover__band{height:70px;background:var(--ink-dark);display:flex;justify-content:flex-end;align-items:center;padding-right:26px}
  .cover__strip{height:40px;background:var(--band-grey)}
  .cover__photo{display:block;margin-top:8px}
  .cover__tagline{position:absolute;left:42px;right:30px;top:436px;font-style:italic;font-weight:400;font-size:16px;line-height:1.25;color:var(--text-grey)}

  .brand{display:flex;flex-direction:column;align-items:flex-start;color:var(--logo-grey)}
  .brand__name{font-weight:300;font-size:38px;line-height:.9;letter-spacing:.5px}
  .brand__sub{font-size:8px;font-weight:400;margin-top:3px;letter-spacing:.2px}

  /* ---------- Inside spread ---------- */
  .spread{position:absolute;left:20px;top:586px;width:944px;height:598px;background:var(--paper);box-shadow:0 2px 8px rgba(0,0,0,.18);display:grid;grid-template-rows:64px 44px 334px 1fr;overflow:hidden}
  .spread__band{background:var(--ink-dark);display:flex;justify-content:space-between;align-items:center;padding:0 24px 0 110px}
  .spread__intro{font-style:italic;font-weight:300;font-size:10px;line-height:1.35;color:#cfcfcf;max-width:380px}
  .spread__band .brand__name{font-size:34px}
  .spread__heading{display:flex;align-items:flex-end;padding:0 0 6px 110px;background:linear-gradient(var(--band-grey),var(--paper))}
  .spread__heading h2{font-weight:300;font-size:17px;letter-spacing:1.5px;color:var(--text-mid)}

  .spread__main{display:grid;grid-template-columns:124px 1fr 124px;overflow:hidden}
  .list-col{padding:4px 4px 0 20px;overflow:hidden}
  .list-col--right{padding:4px 6px 0 12px}
  .list-col h3{font-style:italic;font-weight:400;font-size:11px;line-height:1.2;color:var(--text-mid);margin-bottom:5px}
  .list-group{margin-bottom:5px}
  .list-group h4{font-style:italic;font-weight:600;font-size:6.6px;line-height:1.25;color:var(--text-mid)}
  .list-group li{list-style:none;font-style:italic;font-size:6.2px;line-height:1.22;color:var(--text-soft);white-space:nowrap}
  .list-col h3.sectors{margin-top:3px}

  .photo-grid{display:grid;grid-template-columns:255fr 200fr 50fr 150fr;grid-template-rows:124px 204px;height:328px}
  .photo{position:relative;display:block;width:100%;height:100%}
  .photo__no{position:absolute;left:6px;top:6px;width:11px;height:11px;background:#fff;color:var(--ink-dark);font-size:7px;line-height:11px;text-align:center;font-weight:600}
  .p1{grid-column:1;grid-row:1;background:linear-gradient(160deg,#dedede,#b7b7b5 60%,#8f8f8c)}
  .p3{grid-column:2;grid-row:1;background:linear-gradient(170deg,#9a5d45,#c9b8a4 55%,#6e6a66)}
  .p5{grid-column:3/5;grid-row:1;background:linear-gradient(170deg,#e7e2d8,#b9b2a6 60%,#5e5a57)}
  .p2{grid-column:1;grid-row:2;background:linear-gradient(180deg,#3b3b3b,var(--lime) 40%,var(--lime-deep))}
  .p4{grid-column:2/4;grid-row:2;background:linear-gradient(180deg,#7fb2e0,#d7e8f5 45%,#8a9a7a 75%,#7d7f80)}
  .p6{grid-column:4;grid-row:2;background:linear-gradient(170deg,#dcdcdc,#a7a7a7 60%,#cfcac2)}

  .details{display:grid;grid-template-columns:repeat(6,1fr);gap:14px;padding:10px 24px 8px 110px;background:var(--paper-white);border-top:1px solid #e2e2e2}
  .project{font-size:6.2px;line-height:1.3;color:var(--text-soft);font-style:italic}
  .project__no{display:block;width:9px;height:9px;background:var(--ink-dark);color:#fff;font-style:normal;font-size:6px;line-height:9px;text-align:center;margin-bottom:3px}
  .project dl{display:grid;grid-template-columns:auto 1fr;column-gap:3px}
  .project dt{color:var(--text-mid)}
  .project dd.client{font-weight:600;color:var(--text-mid)}
  .project h5{font-size:6.8px;font-weight:400;color:var(--text-mid);margin-top:4px}
</style>
</head>
<body>

<section class="cover" aria-label="Brochure cover">
  <header class="cover__band">
    <div class="brand"><span class="brand__name">rkm</span><span class="brand__sub">Consulting Services Pty Ltd</span></div>
  </header>
  <div class="cover__strip"></div>
  <svg class="cover__photo" width="390" height="300" viewBox="0 0 390 300" role="img" aria-label="Photograph of an office meeting booth with lime green upholstered seating, a grey table and an artwork on a dark wall">
    <defs>
      <linearGradient id="booth" x1="0" y1="0" x2="1" y2="1">
        <stop offset="0" stop-color="#3a3a38"/>
        <stop offset=".45" stop-color="#7f9a1c"/>
        <stop offset="1" stop-color="#b4cf33"/>
      </linearGradient>
    </defs>
    <polygon points="0,18 350,18 350,300 300,300 300,270 150,270 150,230 40,230 40,180 0,180" fill="url(#booth)"/>
  </svg>
  <p class="cover__tagline">Every project receives a level of dedication, commitment and service to ensure client expectations are exceeded</p>
</section>

<section class="spread" aria-label="Brochure inside spread">
  <header class="spread__band">
    <p class="spread__intro">rkm formed in 1998 to provide highly personalised design and project management service for the commercial market. We employ a handpicked team of Engineer's and Designers, all with a strong sense of Client focus and professionalism.</p>
    <div class="brand"><span class="brand__name">rkm</span><span class="brand__sub">Consulting Services Pty Ltd</span></div>
  </header>

  <div class="spread__heading"><h2>RECENT PROJECTS</h2></div>

  <div class="spread__main">
    <aside class="list-col">
      <h3>Our Disaplines</h3>
      <div class="list-group"><h4>Electrical Services</h4><ul><li>LV Distribution</li><li>Standby Power Generation</li><li>Earthing</li><li>Lightning Protection</li><li>Uninterruptible Power Supplies</li></ul></div>
      <div class="list-group"><h4>Lighting Services</h4><ul><li>Task Lighting</li><li>Feature Lighting</li><li>Sports Lighting</li><li>Roadway Lighting</li><li>Emergency Lighting</li></ul></div>
      <div class="list-group"><h4>Mechanical Services</h4><ul><li>Air Conditioning</li><li>Heating &amp; Ventilation</li><li>Comms Room Cooling</li></ul></div>
      <div class="list-group"><h4>Fire Detection Services</h4><ul><li>Fire Detection &amp; Alarm</li><li>Emergency Warning</li><li>Intercommunication</li></ul></div>
      <div class="list-group"><h4>Communication Services</h4><ul><li>Telephone Distribution</li><li>Communication Distribution</li><li>Communication Rooms</li></ul></div>
      <div class="list-group"><h4>Security Services</h4><ul><li>Intruder Detection &amp; Alarm</li><li>CCTV, Recording &amp; Maintenance</li></ul></div>
      <div class="list-group"><h4>Hydraulic Services</h4><ul><li>Hot &amp; Cold Water Supply</li><li>Waste Water</li></ul></div>
    </aside>

    <div class="photo-grid">
      <div class="photo p1" role="img" aria-label="Photograph of an open-plan office with white desks and black chairs"><span class="photo__no">1</span></div>
      <div class="photo p3" role="img" aria-label="Photograph of a boardroom with a long table and exposed brick wall"><span class="photo__no">3</span></div>
      <div class="photo p5" role="img" aria-label="Photograph of a meeting room with a projection screen and arched windows"><span class="photo__no">5</span></div>
      <div class="photo p2" role="img" aria-label="Photograph of lime green meeting booths with grey tables"><span class="photo__no">2</span></div>
      <div class="photo p4" role="img" aria-label="Photograph of a modern industrial building under a blue sky"><span class="photo__no">4</span></div>
      <div class="photo p6" role="img" aria-label="Photograph of an office lounge corner with a feature chair and rug"><span class="photo__no">6</span></div>
    </div>

    <aside class="list-col list-col--right">
      <h3>Our Services</h3>
      <div class="list-group"><h4>Design</h4><ul><li>Design &amp; Documentation</li><li>Assessment</li><li>Calculation</li><li>Specification</li><li>Client Brief</li></ul></div>
      <div class="list-group"><h4>Feasibility</h4><ul><li>Reporting</li><li>Studies</li><li>Grant Applications</li><li>Life Cycle Cost Analysis</li></ul></div>
      <div class="list-group"><h4>Sustainability</h4><ul><li>Energy Ratings</li><li>Green Ratings</li><li>Photovoltaic</li><li>Controls</li><li>Reporting</li></ul></div>
      <div class="list-group"><h4>Contract Management</h4><ul><li>Change Control Management</li><li>Testing &amp; Commissioning</li><li>Management Inspection</li><li>&amp; Reporting</li></ul></div>
      <h3 class="sectors">Sectors</h3>
      <div class="list-group"><ul><li>Commercial</li><li>Industrial</li><li>Resource Sector</li><li>Sustainability</li><li>Data Centre</li><li>Retail and Hospitality</li><li>Education</li><li>Streetscape</li><li>Residential</li></ul></div>
    </aside>
  </div>

  <div class="details">
    <article class="project">
      <span class="project__no">1</span>
      <dl><dt>Client</dt><dd class="client">: Civic Estates Office</dd><dt>Job Title</dt><dd>: one60 Marlow Street Heritage Building Refurbishments</dd><dt>Value</dt><dd>: 5.5m</dd><dt>Location</dt><dd>: Perth CBD</dd></dl>
      <h5>Disciplines</h5><p>Electrical, Mechanical, Hydraulics, Fire, Security, Communications</p>
      <h5>Description</h5><p>Three heritage buildings in the centre of the city, restored with new services throughout while keeping the original character of the street front facades intact.</p>
    </article>
    <article class="project">
      <span class="project__no">2</span>
      <dl><dt>Client</dt><dd class="client">: Civic Estates Office</dd><dt>Job Title</dt><dd>: one60 Marlow Street Heritage Building Refurbishments</dd><dt>Value</dt><dd>: 5.5m</dd><dt>Location</dt><dd>: Perth CBD</dd></dl>
      <h5>Disciplines</h5><p>Electrical, Mechanical, Hydraulics, Fire, Security, Communications</p>
      <h5>Description</h5><p>Three heritage buildings in the centre of the city, restored with new services throughout while keeping the original character of the street front facades intact.</p>
    </article>
    <article class="project">
      <span class="project__no">3</span>
      <dl><dt>Client</dt><dd class="client">: Civic Estates Office</dd><dt>Job Title</dt><dd>: one60 Marlow Street Heritage Building Refurbishments</dd><dt>Value</dt><dd>: 5.5m</dd><dt>Location</dt><dd>: Perth CBD</dd></dl>
      <h5>Disciplines</h5><p>Electrical, Mechanical, Hydraulics, Fire, Security, Communications</p>
      <h5>Description</h5><p>Three heritage buildings in the centre of the city, restored with new services throughout while keeping the original character of the street front facades intact.</p>
    </article>
    <article class="project">
      <span class="project__no">4</span>
      <dl><dt>Client</dt><dd class="client">: Harlow Brandt</dd><dt>Job Title</dt><dd>: Harlow Brandt Fit Out</dd><dt>Value</dt><dd>: 3.2m</dd><dt>Location</dt><dd>: Perth CBD</dd></dl>
      <h5>Disciplines</h5><p>Electrical, Mechanical and Hydraulics</p>
      <h5>Description</h5><p>A two level office fit out within a newly finished tower, delivered as one coordinated services package with a single point of contact and responsibility for the client.</p>
    </article>
    <article class="project">
      <span class="project__no">5</span>
      <dl><dt>Client</dt><dd class="client">: Civic Estates Office</dd><dt>Job Title</dt><dd>: one60 Marlow Street Heritage Building Refurbishments</dd><dt>Value</dt><dd>: 5.5m</dd><dt>Location</dt><dd>: Perth CBD</dd></dl>
      <h5>Disciplines</h5><p>Electrical, Mechanical, Hydraulics, Fire, Security, Communications</p>
      <h5>Description</h5><p>Three heritage buildings in the centre of the city, restored with new services throughout while keeping the original character of the street front facades intact.</p>
    </article>
    <article class="project">
      <span class="project__no">6</span>
      <dl><dt>Client</dt><dd class="client">: Avery Lane Hall</dd><dt>Job Title</dt><dd>: VESTRA Office Refurbishment</dd><dt>Value</dt><dd>: 1.5m</dd><dt>Location</dt><dd>: 88 Linden Street</dd></dl>
      <h5>Disciplines</h5><p>Electrical, Fire and Security</p>
      <h5>Description</h5><p>Design and documentation of electrical, fire and security services for a new head office, converting an industrial building into bright open workspace.</p>
    </article>
  </div>
</section>

</body>
</html>
```